Powerpoint Template Design

We need a Corporate Powerpoint Template. We are a small boutique IT consultancy specialized in Business Intelligence and Analytics. We typically carry out projects and system implementations for our clients in Singapore and South East Asia region.
You may think: IT, arggg boring folks. No, we're not. We appreciate stylish design.
Attached is our logo that should appear in all slides, larger scale on the title slide and small size in content slides.

Industry/Entity Type

Boutique

```html
<!DOCTYPE html>
<html lang="en">
<head>
<meta charset="utf-8">
<title>Clearspan – Corporate Presentation Template</title>
<link rel="stylesheet" href="https://fonts.googleapis.com/css2?family=Abel&family=Roboto+Condensed:wght@400;700&family=Arimo:wght@400;700&display=swap">
<style>
  :root {
    --stage-bg: #e8e3dc;
    --slide-bg: #ffffff;
    --navy: #123a78;
    --blue: #1c5aa6;
    --cyan: #2ab0d6;
    --ink: #111111;
    --grey: #6d6f73;
    --grey-light: #b9bcc0;
    --text-muted: #8a8c90;
    --green: #7cb342;
  }
  * { box-sizing: border-box; margin: 0; padding: 0; }
  html, body { width: 1200px; height: 670px; overflow: hidden; background: var(--stage-bg); }
  .stage { position: relative; width: 1200px; height: 670px; }
  .defs { position: absolute; width: 0; height: 0; }

  .slide {
    position: absolute; width: 254px; height: 189px; background: var(--slide-bg);
    overflow: hidden; font-family: "Roboto Condensed", sans-serif; color: var(--grey);
  }
  .slide-footer { position: absolute; left: 0; bottom: 0; width: 100%; height: 40px; }

  .slide-heading {
    position: absolute; font-family: "Abel", sans-serif; font-size: 11px;
    color: var(--navy); letter-spacing: .2px; white-space: pre;
  }
  .body-copy { position: absolute; font-size: 4.4px; line-height: 7px; color: var(--text-muted); }
  .bullet-list { position: absolute; list-style: none; font-size: 4.6px; font-weight: 700; color: var(--navy); }
  .bullet-list li { position: relative; padding-left: 9px; }
  .bullet-list li::before {
    content: ""; position: absolute; left: 0; top: 1.5px; width: 3px; height: 3px; background: var(--green);
  }
  .bullet-list.teal li::before { background: #2a8c8c; }

  .photo { position: absolute; }

  /* Title slide */
  .brand-name {
    position: absolute; left: 0; width: 100%; text-align: center;
    font-family: "Abel", sans-serif; color: var(--grey);
  }
  .title-main { position: absolute; width: 100%; text-align: center; font-family: "Abel", sans-serif; font-size: 14px; color: var(--blue); }
  .title-sub { position: absolute; width: 100%; text-align: center; font-family: "Abel", sans-serif; font-size: 11px; color: var(--grey); }

  /* Table slide */
  .data-table { position: absolute; left: 38px; top: 42px; width: 188px; border-collapse: collapse; font-size: 4.4px; color: var(--text-muted); }
  .data-table th {
    height: 17px; font-size: 8.5px; color: #fff; font-weight: 700; text-align: center;
    background: linear-gradient(90deg, var(--cyan), var(--navy) 85%, #1d2a5a);
  }
  .data-table td { height: 13.2px; text-align: center; border-bottom: .5px solid #e2e4e6; border-left: .5px solid #e2e4e6; }
  .data-table td:first-child { border-left: none; }

  /* Two-column slide */
  .sub-columns { position: absolute; left: 28px; top: 42px; width: 210px; display: flex; gap: 16px; }
  .sub-col { flex: 1; font-size: 4.2px; color: var(--text-muted); }
  .sub-col h3 { font-size: 4.6px; font-weight: 700; color: var(--grey); margin: 6px 0 2px 2px; }
  .sub-col h3:first-child { margin-top: 0; }
  .sub-col ul { padding-left: 7px; line-height: 9px; }

  /* Closing slide */
  .thanks { position: absolute; top: 78px; width: 100%; text-align: center; font-family: "Arimo", sans-serif; font-size: 23px; color: var(--ink); }
  .thanks-sub { position: absolute; top: 105px; width: 100%; text-align: center; font-family: "Arimo", sans-serif; font-size: 9px; font-weight: 700; color: var(--navy); }
</style>
</head>
<body>
<svg class="defs" aria-hidden="true">
  <defs>
    <linearGradient id="band" x1="0" x2="1">
      <stop offset="0" stop-color="#1d4f9a"/>
      <stop offset=".5" stop-color="#123a78"/>
      <stop offset="1" stop-color="#2a66b2"/>
    </linearGradient>
    <linearGradient id="cyl" x1="0" x2="1">
      <stop offset="0" stop-color="#123a78"/>
      <stop offset=".5" stop-color="#2a6fb8"/>
      <stop offset="1" stop-color="#123a78"/>
    </linearGradient>
    <linearGradient id="tag" x1="0" x2="1">
      <stop offset="0" stop-color="#2ab0d6"/>
      <stop offset="1" stop-color="#1c3f7a"/>
    </linearGradient>
    <symbol id="footer" viewBox="0 0 254 40" preserveAspectRatio="none">
      <path d="M0,14 Q120,34 254,6 L254,40 L0,40 Z" fill="url(#band)"/>
      <path d="M0,16 Q130,32 254,8" fill="none" stroke="#ffffff" stroke-width="2"/>
      <path d="M40,20 Q160,24 254,2" fill="none" stroke="#b9bcc0" stroke-width="2.2"/>
    </symbol>
  </defs>
</svg>

<main class="stage">

  <!-- Title slide -->
  <section class="slide slide-title" style="left:333px;top:32px">
    <div class="brand-name" style="top:62px;font-size:30px">Clearspan</div>
    <div class="title-main" style="top:113px">TITLE OF PRESENTATION</div>
    <div class="title-sub" style="top:128px">Description</div>
    <svg class="slide-footer"><use href="#footer"/></svg>
  </section>

  <!-- Text + bullets -->
  <section class="slide" style="left:623px;top:32px">
    <h2 class="slide-heading" style="left:38px;top:21px">LOREM IPSUM  LOREM</h2>
    <p class="body-copy" style="left:38px;top:43px;width:178px">Orem ipsum dolor sit amet, consectetuer adipiscing elit, sed diam nonummy nibh euismod tincidunt ut laoreet dolore magna aliquam erat volutpat. Ut wisi enim ad minim veniam, quis nostrud exerci tation ullamcorper suscipit lobortis nisl ut aliquip ex ea commodo consequat. Duis autem vel eum iriure dolor in hendrerit in vulputate velit esse molestie consequat, vel illum dolore eu feugiat nulla facilisis.</p>
    <ul class="bullet-list" style="left:38px;top:98px;line-height:11.5px">
      <li>Lorem ipsum  Lorem Lorem ipsum  Lorem</li>
      <li>Lorem ipsum Lorem Lorem</li>
      <li>Lorem ipsum Lorem Lorem ipsum  Lorem  Lorem ipsum</li>
      <li>Lorem ipsum orem Lorem ipsum  Le</li>
      <li>Lorem ipsum Lorem</li>
    </ul>
    <svg class="slide-footer"><use href="#footer"/></svg>
  </section>

  <!-- Text + wide image -->
  <section class="slide" style="left:903px;top:32px">
    <h2 class="slide-heading" style="left:43px;top:21px">LOREM IPSUM  LOREM</h2>
    <p class="body-copy" style="left:43px;top:43px;width:178px">Orem ipsum dolor sit amet, consectetuer adipiscing elit, sed diam nonummy nibh euismod tincidunt ut laoreet dolore magna aliquam erat volutpat. Ut wisi enim ad minim veniam, quis nostrud exerci tation ullamcorper suscipit lobortis nisl ut aliquip ex ea commodo consequat.</p>
    <div class="photo" role="img" aria-label="Photo of signposts reading summit, global, business and success against a blue sky"
         style="left:0;top:92px;width:254px;height:97px;background:linear-gradient(160deg,#0f3c86,#2a73c4 45%,#5a9ad8 60%,#1b4f9e)"></div>
  </section>

  <!-- Text + side image -->
  <section class="slide" style="left:335px;top:237px">
    <h2 class="slide-heading" style="left:22px;top:20px">LOREM IPSUM</h2>
    <p class="body-copy" style="left:22px;top:40px;width:96px">Lorem ipsum dolor sit amet, consectetuer adipiscing elit, sed diam nonummy nibh euismod tincidunt ut laoreet dolore magna aliquam erat volutpat. Ut wisi enim ad minim veniam, quis nostrud exerci tation ullamcorper suscipit lobortis nisl ut aliquip ex ea commodo consequat. Duis autem vel eum iri.</p>
    <div class="photo" role="img" aria-label="Blue-toned photo of a businessman walking across a floor"
         style="left:131px;top:0;width:123px;height:178px;background:linear-gradient(180deg,#7fa4c6,#2e5d8e 55%,#a9c3da)"></div>
    <svg class="slide-footer"><use href="#footer"/></svg>
  </section>

  <!-- Table -->
  <section class="slide" style="left:623px;top:237px">
    <h2 class="slide-heading" style="left:38px;top:18px">LOREM IPSUM</h2>
    <table class="data-table">
      <thead><tr><th colspan="4">Lorem ipsum  Lorem ipsum  Lorem ipsum</th></tr></thead>
      <tbody>
        <tr><td>Lorem ipsum</td><td>Lorem ipsum</td><td>Lorem ipsum</td><td>Lorem ipsum</td></tr>
        <tr><td>Lorem ipsum</td><td>Lorem ipsum</td><td>Lorem ipsum</td><td>Lorem ipsum</td></tr>
        <tr><td>Lorem ipsum</td><td>Lorem ipsum</td><td>Lorem ipsum</td><td>Lorem ipsum</td></tr>
        <tr><td>Lorem ipsum</td><td>Lorem ipsum</td><td>Lorem ipsum</td><td>Lorem ipsum</td></tr>
        <tr><td>Lorem ipsum</td><td>Lorem ipsum</td><td>Lorem ipsum</td><td>Lorem ipsum</td></tr>
        <tr><td>Lorem ipsum</td><td>Lorem ipsum</td><td>Lorem ipsum</td><td>Lorem ipsum</td></tr>
        <tr><td>Lorem ipsum</td><td>Lorem ipsum</td><td>Lorem ipsum</td><td>Lorem ipsum</td></tr>
      </tbody>
    </table>
    <svg class="slide-footer"><use href="#footer"/></svg>
  </section>

  <!-- Database diagram -->
  <section class="slide" style="left:903px;top:237px">
    <h2 class="slide-heading" style="left:25px;top:18px">LOREM IPSUM</h2>
    <svg class="diagram" width="254" height="189" viewBox="0 0 254 189" style="position:absolute;left:0;top:0"
         font-family="Roboto Condensed, sans-serif" font-size="4.2" font-weight="700" fill="#fff" text-anchor="middle">
      <g stroke="#9aa3ad" stroke-width=".6" fill="none">
        <path d="M33,55 V110 M33,72 H39 M33,100 H39"/>
        <path d="M81,55 V136 M81,72 H86 M81,100 H86 M81,128 H86"/>
        <path d="M127,55 V136 M127,72 H132 M127,100 H132 M127,128 H132"/>
        <path d="M173,55 V136 M173,72 H178 M173,100 H178 M173,128 H178"/>
      </g>
      <g>
        <rect x="30" y="43" width="40" height="12" rx="1.5" fill="url(#tag)"/><text x="50" y="51">Lorem ipsum</text>
        <rect x="78" y="43" width="40" height="12" rx="1.5" fill="url(#tag)"/><text x="98" y="51">Lorem ipsum</text>
        <rect x="124" y="43" width="40" height="12" rx="1.5" fill="url(#tag)"/><text x="144" y="51">Lorem ipsum</text>
        <rect x="170" y="43" width="40" height="12" rx="1.5" fill="url(#tag)"/><text x="190" y="51">Lorem ipsum</text>
      </g>
      <g>
        <path d="M39,63 v17 a14,3.5 0 0 0 28,0 v-17 Z" fill="url(#cyl)"/><ellipse cx="53" cy="63" rx="14" ry="3.5" fill="#3a86cf"/><text x="53" y="75">Lorem</text>
        <path d="M39,91 v17 a14,3.5 0 0 0 28,0 v-17 Z" fill="url(#cyl)"/><ellipse cx="53" cy="91" rx="14" ry="3.5" fill="#3a86cf"/><text x="53" y="103">Lorem</text>

        <path d="M86,63 v17 a14,3.5 0 0 0 28,0 v-17 Z" fill="url(#cyl)"/><ellipse cx="100" cy="63" rx="14" ry="3.5" fill="#3a86cf"/><text x="100" y="75">Lorem</text>
        <path d="M86,91 v17 a14,3.5 0 0 0 28,0 v-17 Z" fill="url(#cyl)"/><ellipse cx="100" cy="91" rx="14" ry="3.5" fill="#3a86cf"/><text x="100" y="103">Lorem</text>
        <path d="M86,119 v17 a14,3.5 0 0 0 28,0 v-17 Z" fill="url(#cyl)"/><ellipse cx="100" cy="119" rx="14" ry="3.5" fill="#3a86cf"/><text x="100" y="131">Lorem</text>

        <path d="M132,63 v17 a14,3.5 0 0 0 28,0 v-17 Z" fill="url(#cyl)"/><ellipse cx="146" cy="63" rx="14" ry="3.5" fill="#3a86cf"/><text x="146" y="75">Lorem</text>
        <path d="M132,91 v17 a14,3.5 0 0 0 28,0 v-17 Z" fill="url(#cyl)"/><ellipse cx="146" cy="91" rx="14" ry="3.5" fill="#3a86cf"/><text x="146" y="103">Lorem</text>
        <path d="M132,119 v17 a14,3.5 0 0 0 28,0 v-17 Z" fill="url(#cyl)"/><ellipse cx="146" cy="119" rx="14" ry="3.5" fill="#3a86cf"/><text x="146" y="131">Lorem</text>

        <path d="M178,63 v17 a14,3.5 0 0 0 28,0 v-17 Z" fill="url(#cyl)"/><ellipse cx="192" cy="63" rx="14" ry="3.5" fill="#3a86cf"/><text x="192" y="75">Lorem</text>
        <path d="M178,91 v17 a14,3.5 0 0 0 28,0 v-17 Z" fill="url(#cyl)"/><ellipse cx="192" cy="91" rx="14" ry="3.5" fill="#3a86cf"/><text x="192" y="103">Lorem</text>
        <path d="M178,119 v17 a14,3.5 0 0 0 28,0 v-17 Z" fill="url(#cyl)"/><ellipse cx="192" cy="119" rx="14" ry="3.5" fill="#3a86cf"/><text x="192" y="131">Lorem</text>
      </g>
    </svg>
    <svg class="slide-footer"><use href="#footer"/></svg>
  </section>

  <!-- Section divider -->
  <section class="slide slide-section" style="left:36px;top:456px">
    <div class="brand-name" style="top:62px;font-size:30px">Clearspan</div>
    <div class="title-main" style="top:112px;font-size:18px">Part 3</div>
    <svg class="slide-footer"><use href="#footer"/></svg>
  </section>

  <!-- Bullet list -->
  <section class="slide" style="left:335px;top:456px">
    <h2 class="slide-heading" style="left:22px;top:18px">LOREM IPSUM</h2>
    <ul class="bullet-list teal" style="left:22px;top:44px;line-height:15px">
      <li>Lorem ipsum dolor sit amet, consectetuer adipiscing elit, sed diam nonummy.</li>
      <li>Lorem ipsum dolor sit amet, consectetuer adipiscing elit, sed diam nonummy.</li>
      <li>Lorem ipsum dolor sit amet, consectetuer adipiscing elit, sed diam nonummy.</li>
      <li>Lorem ipsum dolor sit amet, consectetuer adipiscing elit, sed diam nonummy.</li>
      <li>Lorem ipsum dolor sit amet, consectetuer adipiscing elit, sed diam nonummy.</li>
      <li>Lorem ipsum dolor sit amet, consectetuer.</li>
    </ul>
    <svg class="slide-footer"><use href="#footer"/></svg>
  </section>

  <!-- Two columns with subtitles -->
  <section class="slide" style="left:623px;top:456px">
    <h2 class="slide-heading" style="left:20px;top:18px">LOREM IPSUM</h2>
    <div class="sub-columns">
      <div class="sub-col">
        <h3>Sub Title-1</h3>
        <ul><li>Lorem ipsum dolor sit amet, eiuer.</li><li>Adipiscing elit, sed diam non euismod tincidunt.</li></ul>
        <h3>Sub Title-2</h3>
        <ul><li>Lorem ipsum dolor sit amet, eiuer.</li><li>Adipiscing elit, sed diam non euismod tincidunt.</li></ul>
        <h3>Sub Title-3</h3>
        <ul><li>Lorem ipsum dolor sit amet, eiuer.</li><li>Adipiscing elit, nummy nibh euismod tincidunt.</li></ul>
      </div>
      <div class="sub-col">
        <h3>Sub Title-1</h3>
        <ul><li>Lorem ipsum dolor sit amet, consectetuer.</li></ul>
        <h3>Sub Title-2</h3>
        <ul><li>Lorem ipsum dolor sit amet, consectetuer.</li><li>Adipiscing elit, nonummy nibh euismod tincidunt.</li></ul>
        <h3>Sub Title-3</h3>
        <ul><li>Lorem ipsum dolor sit amet, consectetuer.</li><li>Adipiscing elit, nummy nibh euismod tincidunt.</li></ul>
      </div>
    </div>
    <svg class="slide-footer"><use href="#footer"/></svg>
  </section>

  <!-- Closing slide -->
  <section class="slide slide-closing" style="left:903px;top:456px">
    <div class="thanks">Thank You!</div>
    <div class="thanks-sub">For your attention</div>
    <svg class="slide-footer"><use href="#footer"/></svg>
  </section>

</main>
</body>
</html>
```